Pediatric Dentist Business Card

I need a business card designed for a dentist who works exclusively with children.
We prefer designs that are out of ordiary that is fun and interesting to kids.

there is no logo since this is a dentists office. The name of the doctor is "Tavro Kine" if you want to get creative with that.

Target Market(s)

Kids

Industry/Entity Type

Business

Contact Information for Business Card

Anythings that is creative

Colors

Designer to choose colors to be used in the design.

```html
<!DOCTYPE html>
<html lang="en">
<head>
<meta charset="utf-8">
<title>Tavro Kine – Pediatric Dentist Business Card</title>
<link rel="stylesheet" href="https://fonts.googleapis.com/css2?family=Questrial&family=Roboto:wght@400;500&display=swap">
<style>
  :root {
    --page-bg: #e9e6e1;
    --card-white: #ffffff;
    --brand-blue: #3b44b0;
    --sky-blue: #0aa6e8;
    --deep-indigo: #343a9c;
    --sun-yellow: #ffd21a;
    --sun-orange: #f26a1b;
    --tag-red: #ef4a23;
    --ink: #2b2b2b;
    --icon-yellow: #ffcc1f;
  }
  * { margin: 0; padding: 0; box-sizing: border-box; }
  html, body { width: 1200px; height: 800px; overflow: hidden; }
  body {
    background: var(--page-bg);
    display: flex; align-items: center; justify-content: center;
    font-family: "Questrial", sans-serif;
  }
  .business-card {
    position: relative;
    width: 1050px; height: 600px;
    background: var(--card-white);
    overflow: hidden;
    box-shadow: 0 10px 30px rgba(0,0,0,0.15);
  }
  .wave-art { position: absolute; inset: 0; width: 100%; height: 100%; }
  .brand {
    position: absolute; left: 130px; top: 60px;
    display: flex; align-items: center; gap: 28px;
  }
  .brand-dot {
    width: 110px; height: 110px; border-radius: 50%;
    background: var(--brand-blue);
  }
  .brand-text { display: flex; flex-direction: column; }
  .brand-name {
    font-size: 88px; line-height: 1; font-weight: 400;
    color: var(--brand-blue); letter-spacing: 1px;
  }
  .brand-tagline {
    font-size: 42px; line-height: 1.1; color: var(--tag-red);
    margin-left: 6px;
  }
  .clinic-address {
    position: absolute; left: 60px; top: 212px;
    font-family: "Roboto", sans-serif; font-style: normal;
    font-size: 21px; line-height: 1.35; color: var(--ink);
  }
  .contact-list {
    position: absolute; right: 48px; bottom: 30px;
    list-style: none;
    font-family: "Roboto", sans-serif; font-size: 24px; line-height: 1.55;
    color: var(--card-white); text-align: right;
  }
  .contact-list li { display: flex; align-items: center; justify-content: flex-end; gap: 14px; }
  .contact-icon { width: 22px; height: 22px; flex: none; }
</style>
</head>
<body>
  <article class="business-card">
    <svg class="wave-art" viewBox="0 0 1050 600" aria-hidden="true">
      <defs>
        <linearGradient id="sky-band" x1="0" y1="0" x2="1" y2="0">
          <stop offset="0" stop-color="var(--sky-blue)"/>
          <stop offset="0.6" stop-color="#1aa2e6"/>
          <stop offset="1" stop-color="var(--deep-indigo)"/>
        </linearGradient>
        <linearGradient id="sun-stripe" x1="0" y1="0" x2="1" y2="0">
          <stop offset="0" stop-color="var(--sun-orange)"/>
          <stop offset="0.35" stop-color="var(--sun-yellow)"/>
          <stop offset="1" stop-color="var(--sun-orange)"/>
        </linearGradient>
      </defs>
      <path d="M0,352 C300,338 650,372 1050,350 L1050,600 L0,600 Z" fill="url(#sky-band)"/>
      <path d="M0,328 C300,314 650,348 1050,326" fill="none" stroke="var(--brand-blue)" stroke-width="22"/>
      <path d="M0,302 C300,290 650,318 1050,296" fill="none" stroke="url(#sun-stripe)" stroke-width="12"/>
      <path d="M280,600 C540,480 800,392 1050,382 L1050,600 Z" fill="var(--deep-indigo)"/>
    </svg>

    <header class="brand">
      <span class="brand-dot"></span>
      <div class="brand-text">
        <h1 class="brand-name">Tavro Kine</h1>
        <p class="brand-tagline">Pediatric Dentist</p>
      </div>
    </header>

    <address class="clinic-address">
      2280 Maple Grove Ave Suite 310<br>
      Elmhurst, Il 60126
    </address>

    <ul class="contact-list">
      <li>0481-275-309
        <svg class="contact-icon" viewBox="0 0 24 24"><rect x="3" y="4" width="18" height="13" rx="2" fill="none" stroke="var(--icon-yellow)" stroke-width="2.4"/><rect x="8" y="19" width="8" height="2.4" fill="var(--icon-yellow)"/></svg>
      </li>
      <li>0712-604-593
        <svg class="contact-icon" viewBox="0 0 24 24"><path d="M6 3 L10 3 L11 8 L8.5 9.5 C9.5 12 12 14.5 14.5 15.5 L16 13 L21 14 L21 18 C21 19.5 19.5 21 18 21 C10 21 3 14 3 6 C3 4.5 4.5 3 6 3 Z" fill="var(--icon-yellow)"/></svg>
      </li>
      <li>hello@tavrokine.com
        <svg class="contact-icon" viewBox="0 0 24 24"><rect x="2" y="5" width="20" height="14" rx="1.5" fill="var(--icon-yellow)"/><path d="M3 6 L12 13 L21 6" fill="none" stroke="var(--deep-indigo)" stroke-width="1.8"/></svg>
      </li>
      <li>tavrokinedental.com
        <svg class="contact-icon" viewBox="0 0 24 24"><circle cx="12" cy="12" r="9.5" fill="var(--icon-yellow)"/><path d="M2.5 12 H21.5 M12 2.5 V21.5 M4.5 7 H19.5 M4.5 17 H19.5" stroke="var(--deep-indigo)" stroke-width="1.3" fill="none"/><ellipse cx="12" cy="12" rx="4.5" ry="9.5" fill="none" stroke="var(--deep-indigo)" stroke-width="1.3"/></svg>
      </li>
    </ul>
  </article>
</body>
</html>
```